Flyer to promote an IT Innovation Fest

BLW Spark Jam 2018

We are looking to implement a new Innovation program that uses the Morvane LaunchCrate concept. Team Members will receive a red box that contains a set of 20 flash cards that help them to bring an innovative idea to life (based on a business problem or friction point).
We are looking to create a cover page for our 'Red Box' via way of a 1 page flyer.
We want to call it the 'BLW Spark Jam 2018'. We would like the 1 page flyer to look super cool and also have some kind of cool cartoon imagery to bring it to life.
We also want to incorporate our logo into the page somewhere as well.

Ideally, we'd also like to get a logo called 'Spark Jam' that we could use on some of our collateral as well. I thought it might be best to create the 1 pager flyer first, then we could look to pull a Spark Jam logo off that. Please let me know though whether it would be easier to create the logo first, then create the flyer).

Bluewing Labs are a support business to Bluewing Journeys Group which is the largest travel retailer in Australia. Our IT area has around 150 permanent team members. We have a fun culture and can push the boundaries with our imagery as the flyer will be for internal distribution only.

I have attached the Morvane Flash cards that this 1 pager will be the cover page for.

Target Market(s)

Members of the Bluewing Labs team (internal marketing)

Industry/Entity Type

It Company

Requirements
Must have
• Our BLW Logo
• A super cool, innovative, funky look (with some kind of cartoon imagery)
• We need to be able to edit the flyer to add some text
Nice to have
• Stay within the colour theme of the 'Start Here' page on the Morvane attachment

```html
<!DOCTYPE html>
<html lang="en">
<head>
<meta charset="utf-8">
<title>BLW Spark Jam 2018 – Flyer</title>
<link rel="stylesheet" href="https://fonts.googleapis.com/css2?family=Montserrat:wght@600;700;800&display=swap">
<style>
  :root {
    --stage: #ececec;
    --red-deep: #a3312a;
    --red-bright: #d42029;
    --arrow-shade: rgba(90, 8, 10, 0.38);
    --stripe: rgba(120, 12, 14, 0.55);
    --white: #ffffff;
  }
  html, body {
    margin: 0;
    padding: 0;
    width: 981px;
    height: 1200px;
    overflow: hidden;
    background: var(--stage);
  }
  .flyer {
    position: absolute;
    left: 66px;
    top: 0;
    width: 849px;
    height: 1200px;
    background: var(--red-deep);
    overflow: hidden;
    font-family: "Montserrat", sans-serif;
    color: var(--white);
  }
  .flyer__graphics {
    position: absolute;
    inset: 0;
    width: 849px;
    height: 1200px;
  }
  .brand-mark {
    position: absolute;
    left: 169px;
    top: 110px;
    margin: 0;
    font-size: 177px;
    font-weight: 800;
    line-height: 1;
    letter-spacing: 44px;
  }
  .event-title {
    position: absolute;
    left: 169px;
    top: 286px;
    margin: 0;
    font-size: 112px;
    font-weight: 600;
    line-height: 1;
    letter-spacing: -1px;
  }
  .event-subtitle {
    position: absolute;
    left: 169px;
    top: 397px;
    width: 510px;
    height: 84px;
    margin: 0;
    font-size: 84px;
    font-weight: 600;
    line-height: 1;
  }
  .event-year {
    position: absolute;
    right: 0;
    top: 9px;
    width: 255px;
    height: 64px;
    background: var(--white);
    color: var(--red-bright);
    font-size: 72px;
    font-weight: 700;
    line-height: 64px;
    text-align: center;
  }
</style>
</head>
<body>
  <main class="flyer">
    <svg class="flyer__graphics" viewBox="0 0 849 1200" xmlns="http://www.w3.org/2000/svg">
      <rect class="doodle-backdrop" x="0" y="0" width="849" height="1200" fill="var(--red-deep)" role="img" aria-label="Faint hand-drawn business and idea doodles across the background"/>
      <polygon class="bright-wedge" points="0,454 740,1200 0,1200" fill="var(--red-bright)"/>
      <g class="diagonal-stripes" stroke="var(--stripe)" stroke-width="3">
        <line x1="0" y1="470" x2="720" y2="1200"/>
        <line x1="0" y1="486" x2="705" y2="1200"/>
        <line x1="0" y1="502" x2="690" y2="1200"/>
      </g>
      <path class="arrow arrow--large" d="M0,777 H270 V620 L503,862 L270,1105 V944 H0 Z" fill="var(--arrow-shade)"/>
      <path class="arrow arrow--small" d="M0,976 H88 V905 L201,1017 L88,1130 V1066 H0 Z" fill="var(--arrow-shade)"/>
      <g class="idea-sparks" stroke="var(--white)" stroke-width="9" stroke-linecap="round">
        <line x1="771" y1="624" x2="774" y2="705"/>
        <line x1="607" y1="692" x2="643" y2="728"/>
        <line x1="506" y1="813" x2="595" y2="829"/>
        <line x1="476" y1="946" x2="577" y2="948"/>
      </g>
      <rect class="brain-illustration" x="578" y="753" width="271" height="447" rx="60" fill="rgba(255,255,255,0.12)" role="img" aria-label="White line drawing of a brain sitting on a light bulb base"/>
    </svg>

    <h2 class="brand-mark">BLW</h2>
    <h1 class="event-title">SPARK</h1>
    <p class="event-subtitle">JAM <span class="event-year">2018</span></p>
  </main>
</body>
</html>
```